Financial Advisor / Asset Manager Wix Design

I'm currently hosting with Wix and my first attempt at a website is live at www.bramwellhollowgroup.com Clearly I am not a web designer and I need help making this more catchy, modern, cross-platform compatible, search engine optimized, etc. I've got logos, hex color pallets, and a slew of other graphics. I'm interested in working with a winning designer to write/refine my copy/language to complete the build.

Full set of graphics https://albums.picnestly.io/r83Kd27WQfa5T1mZC do NOT use the CONSULTING graphics as this is for a related business / different website

Target Market(s)

Individuals, small institutions, endowments, non-profits seeking financial advice and asset / portfolio management

Industry/Entity Type

Financial Services

Coding

Coded - Design and coding required

Font styles to use
Other font styles liked:
• AvenirLTStd - Black, Book, and Roman as appropriate

Requirements
Must have
• Complete, cross platform website integrating my existing logo
Nice to have
• Easy to update format for go-forward maintenance

```html
<!DOCTYPE html>
<html lang="en">
<head>
<meta charset="utf-8">
<title>Bramwell Hollow Group — Personalized Financial Advice</title>
<link href="https://fonts.googleapis.com/css2?family=Nunito+Sans:wght@400;600;700;800&display=swap" rel="stylesheet">
<style>
:root{
  --navy:#0e2340;
  --ink:#1b2a44;
  --royal:#0a4fa0;
  --offer:#1a7dcf;
  --sky:#14a5e8;
  --mist:#eef0f2;
  --muted:#4a5568;
  --white:#ffffff;
}
*{box-sizing:border-box;margin:0;padding:0}
html,body{width:1200px;height:4016px;overflow:hidden}
body{font-family:"Nunito Sans",Arial,sans-serif;color:var(--ink);background:var(--mist)}
.page{position:relative;width:1200px;height:4016px;overflow:hidden;background:linear-gradient(#f3f4f6,#e7e9ec)}
.abs{position:absolute}
.btn{position:absolute;display:flex;align-items:center;justify-content:center;font-weight:700;font-size:14px;color:var(--white);text-decoration:none;border-radius:2px}
.btn--royal{background:var(--royal)}
.btn--sky{background:var(--sky)}

/* hero */
.hero{position:absolute;left:0;top:0;width:1200px;height:640px;background:linear-gradient(180deg,#6d7a88 0%,#4d5a63 30%,#34423a 55%,#5b6a60 75%,#8a7d5a 100%)}
.brand{position:absolute;left:89px;top:34px;display:flex;align-items:center;gap:10px;color:var(--white);font-weight:700;font-size:20px;letter-spacing:.5px}
.brand__dot{width:14px;height:14px;border:2px solid var(--white)}
.nav{position:absolute;top:38px;left:628px;display:flex;gap:0;font-size:14px;font-weight:600}
.nav a{position:absolute;color:var(--white);text-decoration:none;white-space:nowrap}
.nav a.is-active{color:var(--sky)}
.hero__title{position:absolute;width:100%;text-align:center;color:var(--white);font-weight:700;font-size:37px;line-height:1}
.hero__sub{position:absolute;width:100%;text-align:center;color:var(--white);font-size:23px;line-height:1}
.hero__mark{position:absolute;left:0;width:100%;top:252px;text-align:center;color:var(--white);font-weight:700;font-size:18px;letter-spacing:2px}

/* who we are */
.label{font-size:16px;font-weight:600;color:var(--royal);letter-spacing:.5px}
.h2{font-weight:700;color:var(--ink)}
.body-text{font-size:15.5px;line-height:24px;color:#2d3748}

/* offer */
.offer-title{position:absolute;top:1216px;width:100%;text-align:center;color:var(--white);font-size:38px;font-weight:600}
.service{position:absolute;top:1290px;width:250px;text-align:center;color:var(--white)}
.service__icon{display:block;margin:0 auto;width:104px;height:104px}
.service__name{margin-top:28px;font-size:17px;font-weight:600}
.service__text{margin-top:22px;font-size:11.5px;line-height:19px;padding:0 10px}
.service .btn{position:relative;margin:22px auto 0;width:112px;height:32px;font-size:12px}

/* serve */
.serve-item{position:absolute;left:615px;display:flex;align-items:center;gap:24px;font-size:17px;font-weight:600;color:var(--ink)}
.serve-item__dot{width:66px;height:66px;border-radius:50%;background:#a9d6ea}

/* why */
.why-title{position:absolute;top:2408px;width:100%;text-align:center;font-size:29px;font-weight:700}
.card{position:absolute;top:2480px;width:231px;height:200px;background:var(--white);box-shadow:0 2px 8px rgba(0,0,0,.12);text-align:center;padding-top:24px}
.card svg{width:56px;height:56px}
.card__name{margin-top:10px;font-size:17px;font-weight:600}
.card__text{margin-top:14px;font-size:12.5px;line-height:19px;padding:0 22px;color:#2d3748}

/* contact */
.form{position:absolute;left:615px;top:3022px;width:585px;height:390px;background:var(--white)}
.form__title{position:absolute;left:0;width:100%;top:36px;text-align:center;font-size:29px;font-weight:700}
.field{position:absolute;border:1px solid #cfd4da;font-size:11.5px;color:#555;padding:8px 15px;background:var(--white)}

/* footer */
.foot-h{position:absolute;top:3636px;color:var(--white);font-size:17px;font-weight:600}
.foot-t{position:absolute;color:#d7dde6;font-size:13px;line-height:19px}
.foot-links a{display:block;color:#d7dde6;font-size:12.5px;text-decoration:none;line-height:24px}
.social{position:absolute;top:3861px;width:30px;height:30px;border-radius:50%;background:var(--royal)}
</style>
</head>
<body>
<div class="page">

  <!-- HERO -->
  <section class="hero" role="img" aria-label="Photograph of a mountain valley with a lake under a cloudy sky">
  </section>
  <div class="brand"><span class="brand__dot"></span>Bramwell Hollow Group</div>
  <nav class="nav">
    <a class="is-active" style="left:0">Home</a>
    <a style="left:78px">About Us</a>
    <a style="left:181px">Services</a>
    <a style="left:276px">FAQ's</a>
  </nav>
  <a class="btn btn--royal" style="left:983px;top:28px;width:128px;height:39px">Contact Us</a>
  <h1 class="hero__title" style="left:-135px;top:138px">Personalized financial advice</h1>
  <p class="hero__sub" style="left:-135px;top:177px">to help you achieve your goals</p>
  <p class="hero__mark">Bramwell Hollow Group</p>
  <h2 class="hero__title" style="left:131px;top:331px">Professional management</h2>
  <p class="hero__sub" style="left:131px;top:371px">to make your money work for you</p>
  <a class="btn btn--sky" style="left:536px;top:452px;width:126px;height:39px">Contact Us</a>

  <svg class="abs" style="left:0;top:470px" width="1200" height="180" viewBox="0 0 1200 180" aria-hidden="true">
    <path d="M0 95 C120 160 230 150 320 100 C420 40 560 60 640 80 C760 110 830 20 930 10 C1030 0 1120 40 1200 50 L1200 180 L0 180Z" fill="var(--sky)"/>
    <path d="M0 120 C110 180 240 170 330 115 C430 60 560 80 650 95 C770 120 850 40 950 30 C1050 20 1130 55 1200 70 L1200 180 L0 180Z" fill="#f1f2f4"/>
  </svg>

  <!-- WHO WE ARE -->
  <div class="abs" role="img" aria-label="Illustration of a charging bull outlined in blue with candlestick chart bars" style="left:86px;top:693px;width:451px;height:343px;background:radial-gradient(ellipse at 55% 55%,#9cc6ea 0%,#cfe2f3 45%,rgba(240,242,244,0) 72%)"></div>
  <p class="abs label" style="left:615px;top:696px">WHO WE ARE</p>
  <h2 class="abs h2" style="left:615px;top:737px;width:500px;font-size:29px;line-height:35px">Bramwell Hollow Group is an investment advisory firm committed to serving as fiduciary to our clients.</h2>
  <p class="abs body-text" style="left:615px;top:869px;width:500px">We always act in the best interests of our clients, including putting your interests ahead of our own. We provide independent financial planning, investment management, and asset management services tailored to your unique needs and circumstances.</p>
  <a class="btn btn--royal" style="left:615px;top:991px;width:128px;height:39px">About Us</a>

  <!-- WHAT WE OFFER -->
  <svg class="abs" style="left:0;top:1100px" width="1200" height="700" viewBox="0 0 1200 700" aria-hidden="true">
    <path d="M0 110 C250 30 700 0 1200 100 L1200 600 L0 600Z" fill="var(--royal)"/>
    <path d="M0 125 C250 45 700 15 1200 115 L1200 600 L0 600Z" fill="var(--offer)"/>
    <path d="M0 590 C200 520 450 510 700 600 C850 650 1000 640 1200 560 L1200 700 L0 700Z" fill="var(--royal)"/>
    <path d="M0 600 C200 540 450 535 700 620 C850 665 1000 655 1200 580 L1200 700 L0 700Z" fill="#f1f2f4"/>
  </svg>
  <h2 class="offer-title">What We Offer</h2>

  <div class="service" style="left:79px">
    <svg class="service__icon" viewBox="0 0 104 104" fill="none" stroke="#fff" stroke-width="3"><rect x="30" y="10" width="44" height="60" rx="3"/><rect x="44" y="40" width="40" height="54" rx="3"/><line x1="50" y1="52" x2="78" y2="52"/><circle cx="24" cy="82" r="12"/></svg>
    <p class="service__name">Financial Planning</p>
    <p class="service__text">Once we have a sense of your financial situation and goals, we typically establish a financial plan ...</p>
    <a class="btn btn--royal">Read More</a>
  </div>
  <div class="service" style="left:342px">
    <svg class="service__icon" viewBox="0 0 104 104" fill="none" stroke="#fff" stroke-width="3"><line x1="14" y1="90" x2="14" y2="30"/><line x1="30" y1="90" x2="30" y2="45"/><line x1="46" y1="90" x2="46" y2="55"/><circle cx="72" cy="40" r="20"/><line x1="10" y1="92" x2="94" y2="92"/></svg>
    <p class="service__name">Asset Management</p>
    <p class="service__text">Many advisors use a screening process to find investments. You may be familiar with stock ...</p>
    <a class="btn btn--sky">Read More</a>
  </div>
  <div class="service" style="left:606px">
    <svg class="service__icon" viewBox="0 0 104 104" fill="none" stroke="#fff" stroke-width="3"><circle cx="56" cy="34" r="22"/><rect x="14" y="70" width="14" height="22"/><rect x="34" y="58" width="14" height="34"/><rect x="54" y="46" width="14" height="46"/><line x1="8" y1="94" x2="96" y2="94"/></svg>
    <p class="service__name">Portfolio Optimization</p>
    <p class="service__text">Your investment portfolio was built with money you earned. It should be customized to reflect your goals ...</p>
    <a class="btn btn--royal">Read More</a>
  </div>
  <div class="service" style="left:869px">
    <svg class="service__icon" viewBox="0 0 104 104" fill="none" stroke="#fff" stroke-width="3"><path d="M40 30 C20 50 24 92 56 92 C88 92 92 50 72 30Z"/><line x1="42" y1="24" x2="70" y2="24"/><circle cx="22" cy="82" r="12"/></svg>
    <p class="service__name">Alternative Investments</p>
    <p class="service__text">The challenges facing investors seeking to build portfolios capable of generating attractive returns with acceptable...</p>
    <a class="btn btn--royal">Read More</a>
  </div>

  <!-- WHO WE SERVE -->
  <div class="abs" role="img" aria-label="Photograph of a mountain lake seen from a slope with wildflowers" style="left:207px;top:1846px;width:329px;height:455px;border-radius:0 70px 0 70px;background:linear-gradient(180deg,#8a96a0 0%,#5f6f78 35%,#3f5a52 65%,#5f8a72 85%,#7b6a86 100%)"></div>
  <p class="abs label" style="left:615px;top:1855px">BRAMWELL HOLLOW GROUP</p>
  <h2 class="abs h2" style="left:615px;top:1878px;font-size:28px">Who We Serve</h2>
  <div class="serve-item" style="top:1936px"><span class="serve-item__dot"></span>Individuals &amp; Families</div>
  <div class="serve-item" style="top:2008px"><span class="serve-item__dot"></span>Small Institutions</div>
  <div class="serve-item" style="top:2080px"><span class="serve-item__dot"></span>Endowments</div>
  <div class="serve-item" style="top:2151px"><span class="serve-item__dot"></span>Non-profits</div>
  <a class="btn btn--sky" style="left:615px;top:2250px;width:128px;height:39px">Contact Us</a>

  <!-- WHY WORK WITH US -->
  <h2 class="why-title">Why Work With Us</h2>
  <div class="card" style="left:89px">
    <svg viewBox="0 0 56 56" fill="none" stroke="var(--ink)" stroke-width="2"><rect x="12" y="8" width="28" height="38" rx="2"/><line x1="18" y1="18" x2="34" y2="18"/><line x1="18" y1="26" x2="34" y2="26"/><line x1="18" y1="34" x2="28" y2="34"/></svg>
    <p class="card__name">You Come First</p>
    <p class="card__text">We always act in the best interests of our clients</p>
  </div>
  <div class="card" style="left:352px">
    <svg viewBox="0 0 56 56" fill="none" stroke="var(--ink)" stroke-width="2"><circle cx="28" cy="28" r="18"/><circle cx="28" cy="24" r="5"/><circle cx="28" cy="10" r="4"/><circle cx="28" cy="46" r="4"/><circle cx="10" cy="28" r="4"/><circle cx="46" cy="28" r="4"/></svg>
    <p class="card__name">Personalized Services</p>
    <p class="card__text">We get to know you in order to service your unique needs</p>
  </div>
  <div class="card" style="left:615px">
    <svg viewBox="0 0 56 56" fill="none" stroke="var(--ink)" stroke-width="2"><circle cx="28" cy="28" r="20"/><circle cx="28" cy="28" r="13"/><line x1="28" y1="20" x2="28" y2="36"/></svg>
    <p class="card__name">Transparent Fees</p>
    <p class="card__text">You'll always know what you pay and how we get paid</p>
  </div>
  <div class="card" style="left:880px">
    <svg viewBox="0 0 56 56" fill="none" stroke="var(--ink)" stroke-width="2"><path d="M6 22 L18 16 L30 24 L38 20 L50 26"/><path d="M14 28 L26 40 L34 36 L44 30"/></svg>
    <p class="card__name">We Give Back</p>
    <p class="card__text">We support and better our local communities</p>
  </div>

  <!-- CTA BAND -->
  <svg class="abs" style="left:0;top:2690px" width="1200" height="300" viewBox="0 0 1200 300" aria-hidden="true">
    <path d="M0 5 L1200 5 L1200 300 L0 300Z" fill="var(--navy)"/>
    <path d="M110 40 C400 80 800 80 1100 40 C800 70 400 70 110 40Z" fill="var(--sky)"/>
    <path d="M0 300 L0 290 C200 240 400 235 600 250 C800 265 1000 240 1200 255 L1200 300Z" fill="var(--sky)"/>
  </svg>
  <h2 class="abs" style="left:89px;top:2818px;width:700px;color:var(--white);font-size:29px;font-weight:700;line-height:35px">Come to Bramwell Hollow Group and find out how we can do better together</h2>
  <a class="btn btn--sky" style="left:983px;top:2829px;width:128px;height:47px">FAQ's</a>

  <!-- CONTACT -->
  <div class="abs" role="img" aria-label="Photograph of jagged mountain peaks glowing orange at sunrise above a pine forest" style="left:0;top:2976px;width:1014px;height:553px;background:linear-gradient(180deg,#b9c9d6 0%,#d99363 30%,#b8643c 50%,#5e4a3a 72%,#24302a 100%)"></div>
  <svg class="abs" style="left:0;top:3430px" width="1200" height="120" viewBox="0 0 1200 120" aria-hidden="true">
    <path d="M0 60 C150 0 250 10 380 50 C520 95 650 40 780 20 C900 5 1050 40 1200 30 L1200 120 L0 120Z" fill="var(--sky)"/>
    <path d="M0 90 C150 30 260 40 390 75 C530 110 660 60 790 45 C910 30 1060 65 1200 55 L1200 120 L0 120Z" fill="var(--navy)"/>
  </svg>
  <div class="form">
    <h2 class="form__title">Get in Touch</h2>
    <div class="field" style="left:56px;top:102px;width:212px;height:34px">First Name</div>
    <div class="field" style="left:285px;top:102px;width:211px;height:34px">Last Name</div>
    <div class="field" style="left:56px;top:156px;width:212px;height:34px">Phone</div>
    <div class="field" style="left:285px;top:156px;width:211px;height:34px">Email ...</div>
    <div class="field" style="left:56px;top:211px;width:440px;height:78px">Leave us a message</div>
    <a class="btn btn--royal" style="left:215px;top:307px;width:128px;height:38px">Submit</a>
  </div>

  <!-- FOOTER -->
  <div class="abs" style="left:0;top:3545px;width:1200px;height:471px;background:var(--navy)"></div>
  <div class="abs" style="left:89px;top:3668px;display:flex;align-items:center;gap:12px;color:#2d8fe0;font-size:26px;font-weight:700;width:240px;line-height:30px">Bramwell Hollow Group</div>

  <p class="foot-h" style="left:385px">Contact Us</p>
  <svg class="abs" style="left:385px;top:3685px" width="16" height="16" viewBox="0 0 16 16" fill="none" stroke="var(--sky)" stroke-width="1.6"><path d="M3 2 L6 2 L7 5 L5 6.5 C6 8.5 7.5 10 9.5 11 L11 9 L14 10 L14 13 C8 13.5 2.5 8 3 2Z"/></svg>
  <p class="foot-t" style="left:406px;top:3684px;font-size:14px">(555) 014-2290</p>
  <svg class="abs" style="left:385px;top:3724px" width="14" height="18" viewBox="0 0 14 18" fill="none" stroke="var(--sky)" stroke-width="1.6"><path d="M7 17 C2 11 1 8 1 6 A6 6 0 0 1 13 6 C13 8 12 11 7 17Z"/><circle cx="7" cy="6" r="2"/></svg>
  <p class="foot-t" style="left:406px;top:3724px">1280 Alder Ridge Rd,<br>Suite #204 Fernvale,<br>VA 20190</p>

  <p class="foot-h" style="left:671px">Quick Links</p>
  <div class="abs foot-links" style="left:671px;top:3676px">
    <a>Home</a><a>About Us</a><a>Services</a><a>FAQ's</a><a>Contact Us</a>
  </div>

  <p class="foot-h" style="left:880px">Sign Up Newsletter</p>
  <div class="field" style="left:880px;top:3683px;width:231px;height:38px;font-size:12px;color:#333;padding-top:11px">Enter your email ...</div>
  <a class="btn btn--sky" style="left:880px;top:3736px;width:95px;height:39px">Send</a>

  <p class="foot-t" style="left:89px;top:3866px;font-size:12.5px">© 2022 <span style="color:var(--sky)">BRAMWELL HOLLOW GROUP.</span> All Right Reserved</p>
  <span class="social" style="left:672px"></span>
  <span class="social" style="left:711px;background:var(--sky)"></span>
  <span class="social" style="left:748px"></span>
  <svg class="abs" style="left:1141px;top:3866px" width="18" height="18" viewBox="0 0 18 18" fill="none" stroke="var(--sky)" stroke-width="2"><path d="M3 16 L9 2 L15 16"/></svg>

  <p class="foot-t" style="left:89px;top:3934px;width:1050px;font-size:12px;line-height:19px">Bramwell Hollow Group LLC ® is a Registered Investment Advisor CRD #482106. We proudly serve as fiduciary to our clients and support our local communities.<br>Bramwell Hollow Group is carbon neutral with the help of greenledgerfund.org</p>

</div>
</body>
</html>
```